Industrial Design Business Card

I am an industrial designer that needs a nice business card that gives a sense of my personal brand (the work I do, how I'm different than others though subtle design). Since I am a designer, myself, the business card needs to have an impeccable design, while feeling like it represents me. Please see the link to my portfolio where you can get a better sense for me.

http://www.markdpelletier.example/

Target Market(s)

Potential employers, industrial designers

Industry/Entity Type

Business

Contact Information for Business Card

Mark Pelletier
Industrial Designer
markpelletierdesign.example
markpelletierdesign@mailbox.example
(555) 218-4370

Font styles to use
Sans Serif

Colors

Designer to choose colors to be used in the design.

Requirements
Must have
• Must have all of the business card details - ideally in that order. If it will look better in a different order, that's fine.
• Simple design - not too flashy. Using a font that is not a pre-set will likely be key to making this simple but also stand out. But also keep somewhat consistent with the fonts and look of my portfolio (markpelletierdesign.example).
• It needs to catch someone's attention while also being simple (not too flashy) design. That is the big challenge.
Should not have
• Random pictures off the internet.

```html
<!DOCTYPE html>
<html lang="en">
<head>
<meta charset="UTF-8">
<title>Mark Pelletier — Business Card</title>
<link href="https://fonts.googleapis.com/css2?family=Montserrat:wght@400;500;700&display=swap" rel="stylesheet">
<style>
  :root {
    --backdrop: #8f8f8f;
    --card: #f1f1ef;
    --ink: #111111;
    --shadow: rgba(0, 0, 0, 0.28);
  }
  * { margin: 0; padding: 0; box-sizing: border-box; }
  html, body {
    width: 1200px;
    height: 1200px;
    overflow: hidden;
  }
  body {
    background: var(--backdrop);
    font-family: "Montserrat", sans-serif;
    color: var(--ink);
    display: flex;
    flex-direction: column;
    align-items: center;
    justify-content: center;
    gap: 60px;
  }
  .card {
    width: 840px;
    height: 480px;
    background: var(--card);
    box-shadow: 0 14px 30px var(--shadow);
    position: relative;
  }
  .card--front {
    display: flex;
    flex-direction: column;
    align-items: center;
  }
  .identity {
    margin-top: 150px;
    text-align: center;
  }
  .identity__name {
    font-weight: 700;
    font-size: 32px;
    letter-spacing: 3px;
    text-transform: uppercase;
  }
  .identity__role {
    font-weight: 500;
    font-size: 21px;
    letter-spacing: 3px;
    text-transform: uppercase;
    margin-top: 6px;
  }
  .contacts {
    position: absolute;
    left: 48px;
    right: 48px;
    bottom: 110px;
    display: flex;
    justify-content: space-between;
    align-items: center;
    list-style: none;
  }
  .contacts__item {
    display: flex;
    align-items: center;
    gap: 8px;
    font-size: 13px;
    font-weight: 500;
    white-space: nowrap;
  }
  .contacts__icon {
    width: 21px;
    height: 21px;
    flex: none;
  }
  .card--back {
    display: flex;
    align-items: center;
    justify-content: center;
    padding: 0 48px;
  }
  .website-banner {
    font-weight: 500;
    font-size: 25px;
    letter-spacing: 5px;
    text-transform: uppercase;
    white-space: nowrap;
  }
</style>
</head>
<body>

  <section class="card card--front" aria-label="Business card front">
    <div class="identity">
      <h1 class="identity__name">Mark Pelletier</h1>
      <p class="identity__role">Industrial Designer</p>
    </div>
    <ul class="contacts">
      <li class="contacts__item">
        <svg class="contacts__icon" viewBox="0 0 24 24" aria-hidden="true">
          <circle cx="12" cy="12" r="12" fill="#111"/>
          <rect x="6.5" y="8" width="11" height="8" fill="none" stroke="#f1f1ef" stroke-width="1.4"/>
          <polyline points="6.5,8 12,12.5 17.5,8" fill="none" stroke="#f1f1ef" stroke-width="1.4"/>
        </svg>
        markpelletierdesign@mailbox.example
      </li>
      <li class="contacts__item">
        <svg class="contacts__icon" viewBox="0 0 24 24" aria-hidden="true">
          <circle cx="12" cy="12" r="12" fill="#111"/>
          <path d="M8.6 6.5c.5-.3 1 0 1.3.5l1 1.9c.2.5.1 1-.3 1.3l-.8.6c.6 1.4 1.6 2.5 3 3.2l.6-.8c.3-.4.9-.5 1.3-.3l1.9 1c.5.3.7.8.5 1.3-.5 1.3-1.6 2-2.9 1.7-3.300-.8-5.8-3.3-6.6-6.6-.3-1.3.4-2.4 1.3-3.1z" fill="#f1f1ef"/>
        </svg>
        (555) 218-4370
      </li>
      <li class="contacts__item">
        <svg class="contacts__icon" viewBox="0 0 24 24" aria-hidden="true">
          <circle cx="12" cy="12" r="12" fill="#111"/>
          <g fill="none" stroke="#f1f1ef" stroke-width="1.2">
            <circle cx="12" cy="12" r="6"/>
            <ellipse cx="12" cy="12" rx="2.6" ry="6"/>
            <line x1="6" y1="12" x2="18" y2="12"/>
            <line x1="7" y1="9" x2="17" y2="9"/>
            <line x1="7" y1="15" x2="17" y2="15"/>
          </g>
        </svg>
        markpelletierdesign.example
      </li>
    </ul>
  </section>

  <section class="card card--back" aria-label="Business card back">
    <p class="website-banner">www.markpelletierdesign.example</p>
  </section>

</body>
</html>
```